2013 Golf Outing Flyer

Our charitable organization was created in honor of my daughter who died at age 16. Our annual fundraiser is a golf tournament. I am not a creative person so I'd like someone to design a printable flyer that grabs people's attention but is not too busy while incorportating our organization's logo with the basic information.

Event details:
3rd Annual Marissa Joan Caldwell Memorial Golf Tournament
4 person scramble

Saturday October 5th, 2013
Larkspur Golf Club, Auburn, IL
9:30 Registration
Shotgun start at noon
To Register go online to www.marissajcaldwellgolf.teesignups.example or email
marissacaldwellfund@mailbox.example

Scholarships to Cedar Rapids Hollow High School seniors are made possible by our orgnization through this fundraiser.
Updates

Target Market(s)

golfers and businesses willing to sponsor event

Industry/Entity Type

School

Requirements
Must have
• single page-easy to print
includes non profit organization logo which I attached (think I did)
Specific information about the tournament- date and location and registration info
Nice to have
• company logo and the golf outing logo but if both are too much, then just the golf logo and the organization name can be at the bottom

```html
<!DOCTYPE html>
<html lang="en">
<head>
<meta charset="utf-8">
<title>3rd Annual Marissa Joan Caldwell Memorial Golf Tournament</title>
<link rel="stylesheet" href="https://fonts.googleapis.com/css2?family=Fira+Sans:wght@300;400;600;700&display=swap">
<style>
  :root {
    --navy: #14295a;
    --white: #ffffff;
    --cream: #f6f7dc;
    --lime: #8cc63f;
    --lime-light: #b5d84a;
    --sky-top: #2f7fc6;
    --sky-low: #a9d2ef;
    --trees: #2e5526;
    --grass: #5d9a2c;
    --grass-light: #86b83c;
  }
  * { margin: 0; padding: 0; box-sizing: border-box; }
  html, body { width: 849px; height: 1200px; overflow: hidden; background: var(--white); }
  .flyer {
    position: relative;
    width: 849px;
    height: 1200px;
    overflow: hidden;
    font-family: "Fira Sans", Arial, sans-serif;
  }
  .course-photo {
    position: absolute;
    inset: 0;
    background: linear-gradient(180deg,
      var(--sky-top) 0%,
      #5a9fd8 30%,
      var(--sky-low) 55%,
      var(--trees) 58.5%,
      var(--grass) 64%,
      var(--grass-light) 78%,
      var(--grass) 100%);
  }
  .title-numeral {
    position: absolute;
    left: 52px;
    top: 20px;
    font-size: 230px;
    font-weight: 700;
    line-height: 1;
    color: var(--navy);
    letter-spacing: -6px;
  }
  .title-suffix {
    position: absolute;
    left: 146px;
    top: 52px;
    font-size: 58px;
    font-weight: 700;
    line-height: 1;
    color: var(--white);
  }
  .title-lines {
    position: absolute;
    left: 221px;
    top: 156px;
    color: var(--white);
    line-height: 1.05;
  }
  .title-name { font-size: 42px; font-weight: 600; display: block; }
  .title-event { font-size: 42px; font-weight: 300; display: block; }
  .format-badge {
    position: absolute;
    left: 82px;
    top: 328px;
    width: 184px;
    height: 184px;
    border-radius: 50%;
    background: var(--lime);
    color: var(--white);
    display: flex;
    flex-direction: column;
    justify-content: center;
    align-items: center;
    line-height: 1;
  }
  .format-size { font-size: 42px; font-weight: 300; }
  .format-type { font-size: 42px; font-weight: 600; }
  .event-details {
    position: absolute;
    left: 512px;
    top: 342px;
    list-style: none;
    color: var(--cream);
    font-size: 25px;
    font-weight: 600;
    line-height: 35px;
    text-shadow: 0 1px 3px rgba(0, 0, 0, 0.35);
  }
  .cause-note {
    position: absolute;
    left: 523px;
    top: 532px;
    width: 300px;
    color: var(--navy);
    font-size: 20px;
    font-weight: 600;
    line-height: 1.2;
    letter-spacing: -0.3px;
  }
  .outing-name {
    position: absolute;
    left: 316px;
    top: 780px;
    width: 220px;
    text-align: center;
    color: var(--navy);
    font-size: 22px;
    font-weight: 600;
    line-height: 1.1;
  }
  .footer-band {
    position: absolute;
    left: 0;
    bottom: 0;
    width: 849px;
    height: 200px;
  }
  .register {
    position: absolute;
    left: 0;
    width: 849px;
    top: 1104px;
    text-align: center;
    color: var(--white);
    font-size: 22px;
    font-weight: 300;
    line-height: 34px;
  }
  .register strong { color: var(--navy); font-weight: 600; }
</style>
</head>
<body>
<main class="flyer">
  <div class="course-photo" role="img" aria-label="Golf course fairway under a blue sky with trees on the horizon and a golf ball on the grass"></div>

  <h1 class="title">
    <span class="title-numeral">3</span>
    <span class="title-suffix">rd</span>
    <span class="title-lines">
      <span class="title-name">Annual Marissa Joan Caldwell</span>
      <span class="title-event">Memorial Golf Tournament</span>
    </span>
  </h1>

  <div class="format-badge">
    <span class="format-size">4 person</span>
    <span class="format-type">scramble</span>
  </div>

  <ul class="event-details">
    <li>Saturday October 5th, 2013</li>
    <li>Larkspur Golf Club,</li>
    <li>Auburn, IL</li>
    <li>9:30 Registration</li>
    <li>Shotgun start at noon</li>
  </ul>

  <p class="cause-note">Scholarships to Cedar Rapids Hollow High School seniors are made possible by our orgnization through this fundraiser.</p>

  <p class="outing-name">MJC Memorial Golf Outing</p>

  <svg class="footer-band" viewBox="0 0 849 200" aria-hidden="true">
    <defs>
      <linearGradient id="bandFill" x1="0" y1="0" x2="0" y2="1">
        <stop offset="0" stop-color="#c3df5a"/>
        <stop offset="1" stop-color="#8cc63f"/>
      </linearGradient>
    </defs>
    <path d="M0 40 C 220 70, 560 30, 849 0 L 849 200 L 0 200 Z" fill="url(#bandFill)"/>
  </svg>

  <p class="register">To Register go online to <strong>www.marissajcaldwellgolf.teesignups.example</strong><br>or email <strong>marissacaldwellfund@mailbox.example</strong></p>
</main>
</body>
</html>
```